Flyer Design & Business Cards

I have tried to make up some flyer and have attached them as info with what we would like included. I would like them made to look more professional and I would like business cards along the same line.

Industry/Entity Type

Business

```html
<!DOCTYPE html>
<html lang="en">
<head>
<meta charset="utf-8">
<title>Seaholm Inn – Business Cards</title>
<link href="https://fonts.googleapis.com/css2?family=Uncial+Antiqua&family=Open+Sans:wght@400;600&display=swap" rel="stylesheet">
<style>
  :root {
    --stage: #d9d9d9;
    --card-blue: #0f5a82;
    --gold: #f4ab3c;
    --accent-red: #c3262e;
    --illustration-tone: #8fc4de;
    --photo-house-top: #7fa9d6;
    --photo-house-bottom: #5b5a55;
    --photo-fire: #b0612a;
    --photo-bar: #4a3a34;
    --line-soft: rgba(244, 171, 60, 0.85);
  }
  * { box-sizing: border-box; margin: 0; padding: 0; }
  html, body { width: 1200px; height: 631px; overflow: hidden; }
  body {
    background: var(--stage);
    position: relative;
    font-family: "Open Sans", sans-serif;
  }
  .card {
    position: absolute;
    width: 490px;
    height: 272px;
    background: var(--card-blue);
    box-shadow: 0 4px 12px rgba(0,0,0,0.25);
    overflow: hidden;
  }
  .card--front { left: 90px; top: 132px; }
  .card--back  { left: 622px; top: 204px; }

  /* Front card */
  .photo-panel {
    position: absolute; left: 0; top: 0;
    width: 176px; height: 100%;
    border-right: 3px solid var(--accent-red);
    display: grid;
    grid-template-rows: 57% 43%;
    grid-template-columns: 1fr 1fr;
    gap: 3px;
    background: var(--card-blue);
  }
  .photo { display: block; }
  .photo--house {
    grid-column: 1 / 3;
    background: linear-gradient(180deg, var(--photo-house-top) 0%, #b7c8d9 45%, var(--photo-house-bottom) 100%);
  }
  .photo--fireside { background: linear-gradient(160deg, #8a6a4c 0%, var(--photo-fire) 60%, #3d2a1f 100%); }
  .photo--bar { background: linear-gradient(180deg, #2f2624 0%, var(--photo-bar) 55%, #8a6d52 100%); }

  .title-frame {
    position: absolute; left: 206px; top: 42px;
    width: 266px; height: 94px;
    border: 1.5px solid var(--line-soft);
    display: flex; align-items: center; justify-content: center;
  }
  .ornament {
    position: absolute; width: 22px; height: 22px;
    background: var(--gold); opacity: 0.55; border-radius: 50%;
  }
  .ornament--tl { left: -11px; top: -11px; }
  .ornament--tr { right: -11px; top: -11px; }
  .ornament--bl { left: -11px; bottom: -11px; }
  .ornament--br { right: -11px; bottom: -11px; }
  .inn-name {
    font-family: "Uncial Antiqua", serif;
    color: var(--gold);
    font-size: 38px;
    line-height: 1.02;
    text-align: center;
    font-weight: 400;
  }
  .address {
    position: absolute; left: 190px; width: 300px; top: 160px;
    font-style: normal;
    color: var(--gold);
    font-size: 16px;
    line-height: 1.32;
    text-align: center;
  }

  /* Back card */
  .rule {
    position: absolute; left: 44px; right: 44px; height: 1.5px;
    background: var(--line-soft);
  }
  .rule--top { top: 22px; }
  .rule--bottom { bottom: 22px; }
  .rule-end {
    position: absolute; width: 20px; height: 14px;
    background: var(--gold); opacity: 0.55; border-radius: 7px;
  }
  .rule-end--tl { left: 18px; top: 16px; }
  .rule-end--tr { right: 18px; top: 16px; }
  .rule-end--bl { left: 18px; bottom: 16px; }
  .rule-end--br { right: 18px; bottom: 16px; }

  .ship-illustration {
    position: absolute; left: 40px; top: 76px;
    width: 160px; height: 112px;
    background: var(--illustration-tone);
  }
  .contact {
    position: absolute; left: 222px; width: 248px; top: 80px;
    text-align: center; color: var(--gold);
  }
  .contact__name { font-size: 26px; font-weight: 600; line-height: 1.2; margin-bottom: 12px; }
  .contact__line { font-size: 18px; line-height: 1.35; }
  .divider-ornament {
    display: block; width: 72px; height: 14px; margin: 16px auto 0;
    background: var(--gold); opacity: 0.55; border-radius: 7px;
  }
</style>
</head>
<body>

<section class="card card--front" aria-label="Business card front">
  <div class="photo-panel">
    <span class="photo photo--house" role="img" aria-label="Photo of the stone inn building under blue sky"></span>
    <span class="photo photo--fireside" role="img" aria-label="Photo of a wood-burning stove by the fireside"></span>
    <span class="photo photo--bar" role="img" aria-label="Photo of bottles on the bar shelf"></span>
  </div>

  <div class="title-frame">
    <span class="ornament ornament--tl" role="img" aria-label="Corner scroll ornament"></span>
    <span class="ornament ornament--tr" role="img" aria-label="Corner scroll ornament"></span>
    <span class="ornament ornament--bl" role="img" aria-label="Corner scroll ornament"></span>
    <span class="ornament ornament--br" role="img" aria-label="Corner scroll ornament"></span>
    <h1 class="inn-name">Seaholm<br>Inn</h1>
  </div>

  <address class="address">
    Seaholm Inn<br>
    Ardnish Bay<br>
    South Tarran<br>
    HX4 2QT
  </address>
</section>

<section class="card card--back" aria-label="Business card back">
  <div class="rule rule--top"></div>
  <div class="rule rule--bottom"></div>
  <span class="rule-end rule-end--tl" role="img" aria-label="Scroll ornament"></span>
  <span class="rule-end rule-end--tr" role="img" aria-label="Scroll ornament"></span>
  <span class="rule-end rule-end--bl" role="img" aria-label="Scroll ornament"></span>
  <span class="rule-end rule-end--br" role="img" aria-label="Scroll ornament"></span>

  <div class="ship-illustration" role="img" aria-label="Illustration area: tall sailing ship at sea"></div>

  <div class="contact">
    <p class="contact__name">Alan Morrow</p>
    <p class="contact__line">01632 960481</p>
    <p class="contact__line">www.seaholminn.com</p>
    <span class="divider-ornament" role="img" aria-label="Scroll ornament"></span>
  </div>
</section>

</body>
</html>
```